Flyer Template

I need a flyer template for door knocking on properties. Text Boxes need to be editable, with a header and text body. Footer to be my info. Project to be stylized to match my real estate signs and logo art from past projects

```html
<!DOCTYPE html>
<html lang="en">
<head>
<meta charset="utf-8">
<title>Branwell Realty – Door Knocking Flyer</title>
<link rel="stylesheet" href="https://fonts.googleapis.com/css2?family=Montserrat:wght@600;700;800&family=Open+Sans:wght@400;700&family=Roboto+Condensed:wght@700&display=swap">
<style>
  :root {
    --red: #d0121b;
    --red-dark: #a70d14;
    --charcoal: #1f1f23;
    --black: #0c0c0d;
    --white: #ffffff;
    --ink: #1b1b1b;
    --muted: #d8d8d8;
  }
  * { margin: 0; padding: 0; box-sizing: border-box; }
  html, body { width: 809px; height: 1200px; overflow: hidden; background: var(--white); }
  .flyer { position: relative; width: 809px; height: 1200px; overflow: hidden; background: var(--white); font-family: "Open Sans", Arial, sans-serif; color: var(--ink); }

  .hero-photo { position: absolute; left: 0; top: 0; width: 809px; height: 560px;
    background: linear-gradient(180deg, #3b4775 0%, #56618b 30%, #6f7389 48%, #4a4a52 70%, #26262b 100%); }
  .hero-glow { position: absolute; left: 200px; top: 230px; width: 500px; height: 160px;
    background: radial-gradient(ellipse at center, rgba(236,226,210,.55) 0%, rgba(236,226,210,0) 70%); }
  .roofline { position: absolute; left: 0; top: 0; width: 809px; height: 60px; }

  .brand { position: absolute; left: 0; top: 58px; width: 809px; text-align: center; color: var(--white); }
  .brand-mark { display: block; width: 40px; height: 40px; margin: 0 auto 12px; border: 4px solid var(--white); }
  .brand-name { font-family: "Montserrat", Arial, sans-serif; font-weight: 700; font-size: 22px; line-height: 1.25; letter-spacing: .5px; }

  .dark-band { position: absolute; left: 0; top: 520px; width: 809px; height: 222px; background: var(--charcoal); }

  .title-band { position: absolute; left: 39px; top: 389px; width: 728px; height: 146px; text-align: center; color: var(--white);
    background: linear-gradient(180deg, var(--red) 0%, var(--red) 60%, var(--red-dark) 60%, var(--red-dark) 100%); }
  .agent-name { font-family: "Montserrat", Arial, sans-serif; font-weight: 800; font-size: 62px; line-height: 1; padding-top: 14px; letter-spacing: .5px; }
  .price-line { font-family: "Montserrat", Arial, sans-serif; font-weight: 700; font-size: 40px; line-height: 1; margin-top: 14px; }
  .price-line sup { font-size: 24px; vertical-align: 14px; }

  .room { position: absolute; top: 574px; width: 220px; color: var(--white); }
  .room h3 { font-family: "Montserrat", Arial, sans-serif; font-weight: 700; font-size: 17px; margin-bottom: 8px; }
  .room p { font-size: 14px; line-height: 1.4; }
  .room-living { left: 68px; } .room-bed { left: 308px; } .room-bath { left: 545px; }

  .room-photo { position: absolute; top: 656px; height: 158px; }
  .photo-living { left: 39px; width: 226px; clip-path: polygon(4% 0, 100% 0, 96% 100%, 0 100%);
    background: linear-gradient(160deg, #3a3f4a 0%, #8a8c90 45%, #cfcac2 100%); }
  .photo-bed { left: 278px; width: 232px; clip-path: polygon(4% 0, 100% 0, 96% 100%, 0 100%);
    background: linear-gradient(150deg, #5a3a22 0%, #8c5e36 40%, #3b3d48 75%, #2c2f3a 100%); }
  .photo-bath { left: 523px; width: 246px; clip-path: polygon(4% 0, 100% 0, 100% 100%, 0 100%);
    background: linear-gradient(160deg, #e8e6e2 0%, #d8d4cc 50%, #e6a83a 62%, #f1ede6 80%); }

  .section-title { font-family: "Montserrat", Arial, sans-serif; font-weight: 700; font-size: 18px; color: var(--red); }
  .section-rule { display: block; width: 112px; height: 3px; background: var(--ink); margin: 8px 0 14px; }
  .about { position: absolute; left: 39px; top: 860px; width: 370px; }
  .about p { font-size: 14.5px; line-height: 1.45; }
  .divider { position: absolute; left: 428px; top: 860px; width: 1px; height: 190px; background: var(--muted); }
  .features { position: absolute; left: 455px; top: 860px; width: 320px; }
  .features ul { list-style: none; display: grid; grid-template-columns: 187px 130px; row-gap: 17px; }
  .features li { display: flex; align-items: center; gap: 12px; font-weight: 700; font-size: 14.5px; }
  .tick { width: 17px; height: 17px; flex: none; }

  .footer { position: absolute; left: 0; top: 1094px; width: 809px; height: 106px; background: var(--black); }
  .footer-phone { position: absolute; left: 0; top: 0; width: 410px; height: 106px; background: var(--red);
    clip-path: polygon(0 0, 96% 0, 100% 100%, 0 100%); display: flex; align-items: center; padding-left: 38px; gap: 14px; color: var(--white); }
  .footer-phone svg { width: 38px; height: 38px; }
  .phone-number { font-family: "Roboto Condensed", Arial, sans-serif; font-weight: 700; font-size: 52px; letter-spacing: .5px; }
  .contact-list { position: absolute; left: 432px; top: 18px; list-style: none; color: var(--white); }
  .contact-list li { display: flex; align-items: center; gap: 18px; font-family: "Montserrat", Arial, sans-serif; font-weight: 700; font-size: 21px; height: 36px; margin-bottom: 6px; }
  .contact-list svg { width: 22px; height: 22px; flex: none; }
</style>
</head>
<body>
<main class="flyer">
  <div class="hero-photo" role="img" aria-label="Photo of a large white two-storey house lit up at dusk">
    <div class="hero-glow"></div>
  </div>
  <svg class="roofline" viewBox="0 0 809 60" aria-hidden="true">
    <polygon points="0,0 809,0 809,38 468,38 404,6 340,38 0,38" fill="var(--white)"/>
    <polyline points="0,38 340,38 404,6 468,38 809,38" fill="none" stroke="var(--red)" stroke-width="5"/>
  </svg>

  <div class="brand">
    <span class="brand-mark"></span>
    <div class="brand-name">BRANWELL<br>REALTY</div>
  </div>

  <div class="dark-band"></div>

  <header class="title-band">
    <h1 class="agent-name">JORDAN BRANWELL</h1>
    <p class="price-line">Price start from - <sup>$</sup>200.00</p>
  </header>

  <section class="room room-living"><h3>Living room</h3><p>Lorem Ipsum is simply dummy text of the printing.</p></section>
  <section class="room room-bed"><h3>bedroom</h3><p>Lorem Ipsum is simply dummy text of the printing.</p></section>
  <section class="room room-bath"><h3>Bathroom</h3><p>Lorem Ipsum is simply dummy text of the printing.</p></section>

  <div class="room-photo photo-living" role="img" aria-label="Photo of a bright living room with large windows"></div>
  <div class="room-photo photo-bed" role="img" aria-label="Photo of a bedroom with wood panelling"></div>
  <div class="room-photo photo-bath" role="img" aria-label="Photo of a white bathroom with a bathtub"></div>

  <section class="about">
    <h2 class="section-title">About us property</h2>
    <span class="section-rule"></span>
    <p>Lorem Ipsum is simply dummy text of the printing and typesetting industry. Lorem Ipsum has been the industry's standard dummy text ever since the 1500s, when an unknown printer took a galley of type and scrambled it to make a type specimen book. It has survived not only five centuries, but also the leap into electronic typesetting, remaining essentially.</p>
  </section>

  <div class="divider"></div>

  <section class="features">
    <h2 class="section-title">Faculties</h2>
    <span class="section-rule"></span>
    <ul>
      <li><svg class="tick" viewBox="0 0 17 17"><rect x="1" y="1" width="15" height="15" fill="none" stroke="var(--red)" stroke-width="2"/><path d="M4 8.5l3 3 6-7" fill="none" stroke="var(--red)" stroke-width="2"/></svg>Lorem ipsum</li>
      <li><svg class="tick" viewBox="0 0 17 17"><rect x="1" y="1" width="15" height="15" fill="none" stroke="var(--red)" stroke-width="2"/><path d="M4 8.5l3 3 6-7" fill="none" stroke="var(--red)" stroke-width="2"/></svg>Lorem ipsum</li>
      <li><svg class="tick" viewBox="0 0 17 17"><rect x="1" y="1" width="15" height="15" fill="none" stroke="var(--red)" stroke-width="2"/><path d="M4 8.5l3 3 6-7" fill="none" stroke="var(--red)" stroke-width="2"/></svg>Lorem ipsum</li>
      <li><svg class="tick" viewBox="0 0 17 17"><rect x="1" y="1" width="15" height="15" fill="none" stroke="var(--red)" stroke-width="2"/><path d="M4 8.5l3 3 6-7" fill="none" stroke="var(--red)" stroke-width="2"/></svg>Lorem ipsum</li>
      <li><svg class="tick" viewBox="0 0 17 17"><rect x="1" y="1" width="15" height="15" fill="none" stroke="var(--red)" stroke-width="2"/><path d="M4 8.5l3 3 6-7" fill="none" stroke="var(--red)" stroke-width="2"/></svg>Lorem ipsum</li>
      <li><svg class="tick" viewBox="0 0 17 17"><rect x="1" y="1" width="15" height="15" fill="none" stroke="var(--red)" stroke-width="2"/><path d="M4 8.5l3 3 6-7" fill="none" stroke="var(--red)" stroke-width="2"/></svg>Lorem ipsum</li>
      <li><svg class="tick" viewBox="0 0 17 17"><rect x="1" y="1" width="15" height="15" fill="none" stroke="var(--red)" stroke-width="2"/><path d="M4 8.5l3 3 6-7" fill="none" stroke="var(--red)" stroke-width="2"/></svg>Lorem ipsum</li>
      <li><svg class="tick" viewBox="0 0 17 17"><rect x="1" y="1" width="15" height="15" fill="none" stroke="var(--red)" stroke-width="2"/><path d="M4 8.5l3 3 6-7" fill="none" stroke="var(--red)" stroke-width="2"/></svg>Lorem ipsum</li>
    </ul>
  </section>

  <footer class="footer">
    <div class="footer-phone">
      <svg viewBox="0 0 24 24" aria-hidden="true"><path fill="var(--white)" d="M6.6 10.8a15.1 15.1 0 0 0 6.6 6.6l2.2-2.2c.3-.3.7-.4 1-.2 1.1.4 2.3.6 3.6.6.6 0 1 .4 1 1V20c0 .6-.4 1-1 1A17 17 0 0 1 3 4c0-.6.4-1 1-1h3.5c.6 0 1 .4 1 1 0 1.3.2 2.5.6 3.6.1.3 0 .7-.2 1z"/></svg>
      <span class="phone-number">555-012-3478</span>
    </div>
    <ul class="contact-list">
      <li><svg viewBox="0 0 24 24" aria-hidden="true"><rect x="2" y="5" width="20" height="14" fill="var(--white)"/><path d="M2 5l10 8 10-8" fill="none" stroke="var(--black)" stroke-width="2"/></svg>info@branwellrealty.com</li>
      <li><svg viewBox="0 0 24 24" aria-hidden="true"><circle cx="12" cy="12" r="10" fill="var(--white)"/><path d="M2 12h20M12 2c-3.5 3-3.5 17 0 20M12 2c3.5 3 3.5 17 0 20" fill="none" stroke="var(--black)" stroke-width="1.6"/></svg>www.branwellrealty.com</li>
    </ul>
  </footer>
</main>
</body>
</html>
```